Harlow Chiropractic Business card

Health related business card, picture on front, logo on back with a spot to schedule multiple appointments.
address, website, email, name of the clinic, chiropractic physician, www.HarlowChiropractic.example P) 615-482-9153 F)615-482-7361, Drpaulharlow@mailbox.example, 418 Bramwell lane Suite 206., Nashville, TN 37298. I would like for it to be professional, with a slight fun and healthy attitude

Industry/Entity Type

Health Care

Contact Information for Business Card

Health related business card, picture on front, logo on back with appointment times.
address, website, email, name of the clinic, chiropractic physician, www.HarlowChiropractic.example P) 615-482-9153 F)615-482-7361, Drpaulharlow@mailbox.example, 418 Bramwell lane Suite 206., Nashville, TN 37298

Font styles to use
Sans Serif

Colors
3176b5
33b8a4
0255a3
00a990
feeeee

Requirements
Must have
• Dr. Paul Harlow, or Paul Harlow, D.C., I want rounded corners, picture on front

```html
<!DOCTYPE html>
<html lang="en">
<head>
<meta charset="utf-8">
<title>Harlow Chiropractic – Business Card</title>
<link rel="stylesheet" href="https://fonts.googleapis.com/css2?family=Open+Sans:wght@400;600&family=Roboto:wght@500;700&display=swap">
<style>
  :root {
    --backdrop: #6e5340;
    --card: #ffffff;
    --brand-blue: #0255a3;
    --text-blue: #1c4f93;
    --brand-green: #6cbf3e;
    --ink: #2a2a2a;
    --rule: #222222;
    --photo-top: #c9ced6;
    --photo-bottom: #8e99ab;
  }
  * { margin: 0; padding: 0; box-sizing: border-box; }
  html, body { width: 1200px; height: 1000px; overflow: hidden; }
  body { background: var(--backdrop); position: relative; font-family: "Open Sans", sans-serif; }

  .card {
    position: absolute; left: 265px; width: 665px; height: 397px;
    background: var(--card); border-radius: 22px; overflow: hidden;
    box-shadow: 0 6px 14px rgba(0,0,0,.35);
  }
  .card--front { top: 73px; }
  .card--back { top: 533px; }

  /* Front */
  .brand-mark { position: absolute; left: 36px; top: 52px; display: flex; align-items: center; gap: 10px; }
  .brand-mark__dot { width: 26px; height: 26px; border-radius: 50%; background: var(--brand-green); }
  .brand-mark__name { font-weight: 600; font-size: 30px; color: var(--brand-blue); line-height: 1; }
  .brand-mark__url { position: absolute; left: 72px; top: 122px; font-size: 9px; letter-spacing: 1.6px; color: var(--brand-blue); }

  .contact { position: absolute; left: 130px; top: 157px; color: var(--ink); font-size: 16px; line-height: 22.5px; }
  .contact__clinic { color: var(--text-blue); font-size: 18px; line-height: 26px; }
  .contact__address { margin-bottom: 8px; }
  .contact__row { display: flex; align-items: center; gap: 6px; }
  .contact__row svg { width: 14px; height: 14px; fill: var(--text-blue); flex: none; }

  .portrait {
    position: absolute; left: 425px; top: 20px; width: 240px; height: 330px;
    background: linear-gradient(180deg, var(--photo-top), var(--photo-bottom));
  }
  .wave { position: absolute; left: 0; top: 0; width: 665px; height: 397px; }
  .doctor { position: absolute; right: 32px; top: 337px; text-align: right; color: #fff; }
  .doctor__name { font-family: "Roboto", sans-serif; font-weight: 700; font-size: 19px; line-height: 24px; }
  .doctor__title { font-size: 16px; line-height: 22px; }

  /* Back */
  .back-brand { position: absolute; left: 0; right: 0; top: 40px; text-align: center; }
  .back-brand__name { font-weight: 600; font-size: 44px; color: var(--brand-blue); line-height: 1.1; }
  .back-brand__url { font-size: 10px; letter-spacing: 2px; color: var(--brand-blue); margin-top: 4px; }
  .appointments__title { position: absolute; left: 0; right: 0; top: 152px; text-align: center;
    font-family: "Roboto", sans-serif; font-weight: 700; font-size: 17px; color: var(--text-blue); }
  .appointment-row { position: absolute; left: 32px; width: 610px; height: 22px; color: var(--text-blue); font-size: 16px; }
  .appointment-row span { position: absolute; top: 0; }
  .appointment-row .line { position: absolute; top: 17px; height: 1.5px; background: var(--rule); }
  .appointment-row .date-line { left: 48px; width: 230px; }
  .appointment-row .time-line { left: 335px; width: 188px; }
  .appointment-row .time-label { left: 290px; }
  .appointment-row .meridiem { left: 535px; }
  .notice { position: absolute; left: 0; right: 0; top: 346px; text-align: center; font-size: 16.5px;
    letter-spacing: .4px; color: var(--text-blue); }
</style>
</head>
<body>

<section class="card card--front">
  <div class="brand-mark">
    <div class="brand-mark__dot"></div>
    <div class="brand-mark__name">Harlow Chiropractic</div>
  </div>
  <div class="brand-mark__url">www.HarlowChiropractic.example</div>

  <div class="portrait" role="img" aria-label="Portrait photo of Dr. Paul Harlow in shirt and tie"></div>

  <div class="contact">
    <div class="contact__clinic">Harlow Chiropractic</div>
    <div>418 Bramwell lane Suite 206.</div>
    <div class="contact__address">Nashville, TN 37298</div>
    <div class="contact__row"><svg viewBox="0 0 24 24"><path d="M6.6 10.8a15.1 15.1 0 0 0 6.6 6.6l2.2-2.2c.3-.3.7-.4 1-.2 1.1.4 2.3.6 3.6.6.6 0 1 .4 1 1V20c0 .6-.4 1-1 1A17 17 0 0 1 3 4c0-.6.4-1 1-1h3.5c.6 0 1 .4 1 1 0 1.3.2 2.5.6 3.6.1.3 0 .7-.2 1z"/></svg>615-482-9153</div>
    <div class="contact__row"><svg viewBox="0 0 24 24"><path d="M6 2h12v5H6zM3 8h18a1 1 0 0 1 1 1v7h-4v5H6v-5H2V9a1 1 0 0 1 1-1zm5 8v3h8v-3z"/></svg>615-482-7361</div>
    <div class="contact__row"><svg viewBox="0 0 24 24"><path d="M2 5h20v14H2zm2 2v.5l8 5 8-5V7z"/></svg>Drpaulharlow@mailbox.example</div>
    <div class="contact__row"><svg viewBox="0 0 24 24"><path d="M12 2a10 10 0 1 0 0 20 10 10 0 0 0 0-20zm0 2c1 1.3 1.8 3 2.1 5H9.9C10.2 7 11 5.3 12 4zm-7.7 7h3.6c0 .7.1 1.4.2 2H4.4a8 8 0 0 1-.1-2zm5.6 0h4.2c0 .7-.1 1.4-.2 2H10c-.1-.6-.1-1.3-.1-2zm6.2 0h3.6a8 8 0 0 1-.1 2h-3.7c.1-.6.2-1.3.2-2zM12 20c-1-1.3-1.8-3-2.1-5h4.2c-.3 2-1.1 3.7-2.1 5z"/></svg>www.HarlowChiropractic.example</div>
  </div>

  <svg class="wave" viewBox="0 0 665 397" aria-hidden="true">
    <path d="M0 300 C150 330 300 348 440 346 L440 351 C300 358 120 350 0 326 Z" fill="var(--brand-green)"/>
    <path d="M0 337 C200 362 420 366 540 330 C600 312 640 296 665 286 L665 397 L0 397 Z" fill="var(--brand-blue)"/>
  </svg>

  <div class="doctor">
    <div class="doctor__name">Dr. Paul Harlow</div>
    <div class="doctor__title">chiropractic physician</div>
  </div>
</section>

<section class="card card--back">
  <div class="back-brand">
    <div class="back-brand__name">Harlow Chiropractic</div>
    <div class="back-brand__url">www.HarlowChiropractic.example</div>
  </div>

  <div class="appointments__title">Next Appointment</div>

  <div class="appointment-row" style="top:192px"><span>Date</span><div class="line date-line"></div><span class="time-label">Time</span><div class="line time-line"></div><span class="meridiem">am&nbsp; / pm</span></div>
  <div class="appointment-row" style="top:230px"><span>Date</span><div class="line date-line"></div><span class="time-label">Time</span><div class="line time-line"></div><span class="meridiem">am&nbsp; / pm</span></div>
  <div class="appointment-row" style="top:268px"><span>Date</span><div class="line date-line"></div><span class="time-label">Time</span><div class="line time-line"></div><span class="meridiem">am&nbsp; / pm</span></div>
  <div class="appointment-row" style="top:305px"><span>Date</span><div class="line date-line"></div><span class="time-label">Time</span><div class="line time-line"></div><span class="meridiem">am&nbsp; / pm</span></div>

  <div class="notice">If you are unable to keep your appointment , please allow 24 hours notice</div>
</section>

</body>
</html>
```